Labels for new organic cosmetics/personal care brand called Verimo

I need labels for new cosmetic brand named ( Verimo )
It is natural and organic
products include:
**natural soaps 3 in a box ( 7 types): shea butter soap, almond soap, lavender soap, apricot soap, olive soap , camel milk soap and sensitive skin soap.

**Organic shea butters (7 types) (in round container) pure shea butter, Shea butter with argan oil, shea butter with olive oil, shea butter with oats, Shea butter with camel milk, shea butter with camel milk and Agarwood and shea butter with donky milk.

**deodorant: one type only , a crystal deodorant.

**shampoo (in cylindrical container) : one type natural shampoo

** Organic Oils (two types) (in clyndrical container) : Argan oil and Rose hip oil.

attached examples of similar containers and outline of labels that i want to have new ones.
**notice:
shape of shea butter container is round and flat.
shape of shampoo is cylindrical.
shape of soaps is a cuboid box.

Target Market(s)

men and women of all ages

Industry/Entity Type

Cosmetics

Font styles to use
Sans Serif

Colors
e4daeb
f9d9e8
fbd4d5
fee3d5
fce8d3
fff3d1
fdf9cf
cee9f5
cadf82

Requirements
Must have
• * Verimo logo
• * organic/natural theme
• * front and back labels
• * 7 labels for soaps, 7 back and 7 front labels for shea butter, one label for deoderant, one label for shampoo, two labels for natural oils.
Nice to have
• leaves, green colors or natural shades of colors , pastel colors
• the color is not specified
Should not have
• **I don't need the container design** .
• just the labels. attached are outline example of the labels and photos of the products so you know the shape of container.
• shape of shea butter container is round and flat.
• shape of shampoo is cylindrical.
• shape of soaps is a cuboid box.

```html
<!DOCTYPE html>
<html lang="en">
<head>
<meta charset="utf-8">
<title>Verimo Soap Labels</title>
<link rel="stylesheet" href="https://fonts.googleapis.com/css2?family=Dancing+Script:wght@700&family=Open+Sans:wght@600;800&display=swap">
<style>
  :root {
    --backdrop: #eeecea;
    --kraft: #b49b7b;
    --kraft-shade: #a88e6d;
    --leaf-green: #a9d23c;
    --earth-brown: #8b3819;
    --small-ink: #7a3a22;
  }
  * { margin: 0; padding: 0; box-sizing: border-box; }
  html, body { width: 1200px; height: 1087px; overflow: hidden; }
  body { background: var(--backdrop); position: relative; }

  /* Front soap sleeve label */
  .label {
    position: absolute;
    width: 340px;
    height: 415px;
    background: repeating-linear-gradient(90deg, var(--kraft) 0 2px, var(--kraft-shade) 2px 3px);
    display: flex;
    flex-direction: column;
    align-items: center;
    padding-top: 36px;
  }
  .label--olive { left: 185px; top: 62px; --ink: var(--leaf-green); }
  .label--oats  { left: 640px; top: 440px; --ink: var(--earth-brown); }

  .brand-name {
    font-family: "Open Sans", sans-serif;
    font-weight: 800;
    font-size: 50px;
    line-height: 1;
    letter-spacing: 1px;
    color: var(--ink);
    margin-bottom: 22px;
  }
  .product-name {
    font-family: "Dancing Script", cursive;
    font-weight: 700;
    color: var(--ink);
    text-align: center;
    line-height: 1.2;
  }
  .product-name__main { display: block; font-size: 62px; }
  .product-name__sub  { display: block; font-size: 46px; margin-top: 8px; }

  .flourish {
    width: 110px;
    height: 26px;
    margin-top: 24px;
    border-radius: 13px;
    background: var(--ink);
    opacity: 0.3;
  }
  .ingredients {
    margin-top: auto;
    margin-bottom: 6px;
    align-self: flex-start;
    padding-left: 46px;
    font-family: "Open Sans", sans-serif;
    font-weight: 600;
    color: var(--small-ink);
    line-height: 1.2;
  }
  .ingredients__title { font-size: 11px; display: block; }
  .ingredients__list  { font-size: 8px; display: block; }
</style>
</head>
<body>
  <section class="label label--olive">
    <div class="brand-name">Verimo</div>
    <h1 class="product-name">
      <span class="product-name__main">Shea Butter</span>
      <span class="product-name__sub">with Olive Oil</span>
    </h1>
    <div class="flourish" role="img" aria-label="Decorative scroll ornament"></div>
    <p class="ingredients">
      <span class="ingredients__title">Ingredients</span>
      <span class="ingredients__list">Shea butter, olive oil, water</span>
    </p>
  </section>

  <section class="label label--oats">
    <div class="brand-name">Verimo</div>
    <h1 class="product-name">
      <span class="product-name__main">Shea Butter</span>
      <span class="product-name__sub">with Oats</span>
    </h1>
    <div class="flourish" role="img" aria-label="Decorative scroll ornament"></div>
    <p class="ingredients">
      <span class="ingredients__title">Ingredients</span>
      <span class="ingredients__list">Shea butter, oats, water</span>
    </p>
  </section>
</body>
</html>
```